Harbor Lane Coaching

We would like to refresh the design of our current website. We want to make it cleaner, more open and more professional looking using simple page layouts and crisp fonts. The site should be lighter and be easy to navigate.

It is important that it be easy to add and change content.

The current site can be seen at www.harborlanecoach.example

As part of this, we want our logo colors to be darker blue and green more professional than they are currently. The current logo is attached as you can see the colors are too "neon"

THIS IS A WEBSITE DESIGN REFRESH PROJECT

Target Market(s)

Executives

Industry/Entity Type

Cleaner

Font styles to use
Sans Serif

Colors
0355a3
cfdfed
9bcb3c

Requirements
Must have
• Ease of use, ease of adding content
Should not have
• No crazy colors, not too busy...

```html
<!DOCTYPE html>
<html lang="en">
<head>
<meta charset="utf-8">
<title>Harbor Lane Coaching</title>
<link href="https://fonts.googleapis.com/css2?family=Oswald:wght@400&family=Open+Sans:ital,wght@0,400;0,600;1,400;1,600&family=Arimo:wght@400&display=swap" rel="stylesheet">
<style>
:root{
  --blue:#0355a3;
  --green:#9bcb3c;
  --light:#cfdfed;
  --page:#e4edf6;
  --footer:#eef3f8;
  --bar:#c6d9ec;
  --text:#3a5570;
  --dark:#1d2a36;
  --rule:#9fb7d0;
  --control:#7f93a8;
}
*{margin:0;padding:0;box-sizing:border-box}
html,body{width:876px;height:1200px;overflow:hidden;background:var(--page)}
body{font-family:"Open Sans",Arial,sans-serif;color:var(--text)}
h1,h2,h3,h4{font-weight:400}
.page{position:relative;width:876px;height:1200px;overflow:hidden;background:var(--page)}
.abs{position:absolute}

.header{left:0;top:0;width:876px;height:108px;background:linear-gradient(180deg,#c9dcee,#d6e4f1)}
.brand-panel{left:64px;top:10px;width:276px;height:98px}
.brand-name{left:84px;top:66px;font-size:23px;font-weight:400;color:var(--blue);letter-spacing:-.3px}
.brand-dot{left:150px;top:26px;width:26px;height:26px;border-radius:50%;background:var(--blue)}
.brand-tag{left:86px;top:93px;font-size:5px;letter-spacing:.4px;text-transform:uppercase;color:#5d7790}
.contact-line{font-family:"Oswald",Arial,sans-serif;font-size:11.5px;color:#1a2430;display:flex;align-items:center;gap:6px}
.contact-line svg{flex:none}

.nav{left:0;top:108px;width:876px;height:34px;background:linear-gradient(180deg,#f7f7f7,#e6e6e6);border-bottom:1px solid #d2d2d2}
.nav ul{list-style:none;display:flex;position:absolute;left:64px;top:0;height:34px}
.nav li{font-family:"Arimo",Arial,sans-serif;font-size:11px;color:#1d1d1d;height:34px;line-height:34px;text-align:center;border-right:1px solid #d8d8d8;box-shadow:1px 0 0 #fff}
.nav li.active{background:var(--green);color:#fff}

.hero-bg{left:0;top:142px;width:876px;height:334px;background:linear-gradient(90deg,#edf3f9,#dde8f2 10%,#dde8f2 90%,#edf3f9)}
.hero{left:64px;top:142px;width:748px;height:334px;background:linear-gradient(100deg,#dfe9f3 0%,#c4d3e2 30%,#aebdcc 55%,#c9d7e4 80%,#e9f0f7 100%)}
.hero-title{left:134px;top:172px;font-style:italic;font-weight:600;font-size:42px;color:var(--blue);letter-spacing:-1px}
.hero-shadow{left:40px;top:474px;width:796px;height:14px;background:radial-gradient(ellipse at 50% 0,rgba(40,60,90,.35),rgba(40,60,90,0) 70%)}
.slider-control{top:286px;width:32px;height:40px;display:flex;align-items:center;justify-content:center}

.sec-title{font-family:"Oswald",Arial,sans-serif;font-weight:400;font-size:13.5px;color:var(--blue);text-transform:uppercase;display:flex;align-items:center;gap:8px;white-space:nowrap}
.sec-title::after{content:"";flex:1;height:3px;background:repeating-linear-gradient(90deg,var(--rule) 0 1px,transparent 1px 3px);margin-top:2px}
.body-text{font-size:8.2px;line-height:14.4px;color:var(--text);text-align:justify}
.service-photo{width:225px;height:120px}
.service-title{font-size:11.5px;font-weight:400;color:var(--dark)}
.service-title.lead{color:var(--blue)}
.service-sub{font-size:7.8px;font-style:italic;font-weight:600;color:var(--dark);margin-top:5px}
.service-text{font-size:8.2px;line-height:14.4px;color:var(--text);margin-top:2px;text-align:justify}
.read-more{font-size:7.8px;font-weight:600;color:var(--dark);text-align:right}
.read-more.lead{color:var(--blue)}

.ask-item{left:64px;width:350px;border-bottom:1px dotted var(--rule);font-size:8.2px;line-height:11px;color:var(--text);display:flex;gap:8px;padding-bottom:7px}
.ask-mark{flex:none;width:9px;height:9px;border-radius:50%;background:var(--blue);margin-top:1px}
.slide-btn{width:23px;height:17px;border:1px solid var(--blue);display:flex;align-items:center;justify-content:center}
.slide-btn.on{background:var(--blue)}

.footer{left:0;top:997px;width:876px;height:163px;background:var(--footer);border-top:2px solid #d5e0eb}
.foot-title{font-size:9px;font-weight:400;color:var(--blue);text-transform:uppercase;display:flex;align-items:center;gap:8px;white-space:nowrap}
.foot-title::after{content:"";flex:1;height:3px;background:repeating-linear-gradient(90deg,var(--rule) 0 1px,transparent 1px 3px)}
.foot-row{font-size:8.2px;line-height:12px;color:var(--text);display:flex;gap:9px;align-items:flex-start}
.foot-row svg{flex:none;margin-top:1px}
.field{background:#f4f6f9;border:1px solid #d6dde5;font-size:7.8px;font-style:italic;color:#8a99a8;padding:4px 6px;height:17px}
.submit{left:757px;top:1121px;width:55px;height:20px;background:var(--blue);color:#fff;font-size:8.6px;text-align:center;line-height:20px}
.social{width:24px;height:24px;border-radius:50%;background:#3b3f44}
.social.first{background:var(--blue)}

.bottom-bar{left:0;top:1160px;width:876px;height:40px;background:var(--bar)}
.bottom-links{left:64px;top:1174px;font-size:8.2px;color:#4f6c88}
.bottom-links .cur{color:#1d2a36}
.bottom-links .sep{color:#8ea6bd;margin:0 4px}
.copyright{right:86px;top:1174px;font-size:8.2px;color:#4f6c88}
.copy-dot{left:792px;top:1171px;width:14px;height:14px;border-radius:50%;background:var(--blue)}
</style>
</head>
<body>
<div class="page">

  <div class="abs header"></div>
  <svg class="abs brand-panel" width="276" height="98" viewBox="0 0 276 98" aria-hidden="true">
    <defs><linearGradient id="panelFill" x1="0" y1="0" x2="0" y2="1"><stop offset="0" stop-color="#f7fafd"/><stop offset="1" stop-color="#e1eaf3"/></linearGradient></defs>
    <path d="M4 0 H218 Q224 0 227 6 L276 98 H0 V4 Q0 0 4 0Z" fill="url(#panelFill)"/>
  </svg>
  <div class="abs brand-dot"></div>
  <div class="abs brand-name">Harbor Lane Coaching</div>
  <div class="abs brand-tag">Coaching leaders and companies from distress to success</div>

  <div class="abs contact-line" style="left:566px;top:32px">
    <svg width="13" height="17" viewBox="0 0 13 17"><path d="M6.5 1A5.5 5.5 0 0 0 1 6.5C1 10.5 6.5 16 6.5 16S12 10.5 12 6.5A5.5 5.5 0 0 0 6.5 1Z" fill="none" stroke="#0355a3" stroke-width="1.8"/><circle cx="6.5" cy="6.5" r="2" fill="#0355a3"/></svg>
    218 Quayside Avenue Suite 40-B Marlow, VA 20999
  </div>
  <div class="abs contact-line" style="left:566px;top:66px">
    <svg width="14" height="14" viewBox="0 0 14 14"><path d="M3 1 L5.5 4 L4 6 Q5.5 9 8 10 L10 8.5 L13 11 L11 13.5 Q5 13 1 4 Z" fill="#0355a3"/></svg>
    (555) 014-7720
  </div>
  <div class="abs contact-line" style="left:672px;top:65px">
    <svg width="16" height="13" viewBox="0 0 16 13"><rect x="1" y="2" width="14" height="10" fill="none" stroke="#0355a3" stroke-width="1.6"/><path d="M1 2 L8 8 L15 2" fill="none" stroke="#0355a3" stroke-width="1.6"/></svg>
    info@harborlanecoach.example
  </div>

  <nav class="abs nav">
    <ul>
      <li class="active" style="width:70px">HOME</li>
      <li style="width:94px">ABOUT US</li>
      <li style="width:130px">WHY COACHING</li>
      <li style="width:91px">SERVICES</li>
      <li style="width:89px">CLIENTS</li>
      <li style="width:106px">RESOURCES</li>
      <li style="width:70px">BLOG</li>
      <li style="width:98px;border-right:0;box-shadow:none">CONTACT US</li>
    </ul>
  </nav>

  <div class="abs hero-bg"></div>
  <div class="abs hero" role="img" aria-label="Photo of a smiling team of executives around a glass meeting table in a bright office"></div>
  <div class="abs hero-title">...To Trust</div>
  <div class="abs slider-control" style="left:20px" aria-label="Previous slide">
    <svg width="14" height="26" viewBox="0 0 14 26"><path d="M12 2 L2 13 L12 24" fill="none" stroke="var(--control)" stroke-width="2.5" stroke-linecap="round" stroke-linejoin="round"/></svg>
  </div>
  <div class="abs slider-control" style="left:824px" aria-label="Next slide">
    <svg width="14" height="26" viewBox="0 0 14 26"><path d="M2 2 L12 13 L2 24" fill="none" stroke="var(--control)" stroke-width="2.5" stroke-linecap="round" stroke-linejoin="round"/></svg>
  </div>
  <div class="abs hero-shadow"></div>

  <h2 class="abs sec-title" style="left:64px;top:496px;width:748px">Welcome to our site!</h2>
  <p class="abs body-text" style="left:64px;top:518px;width:748px">Harbor Lane Coaching works with executives and companies that are facing issues ranging from mild dysfunction to significant distress. We help them pivot, regain control and achieve renewed growth. Harbor Lane Coaching employs the Clear Path Leadership process developed by Dana R. Whitfield PhD., founder of the Institute for Applied Coaching Studies (IACS). Clear Path Leadership is the process that develops a personally effective style of leadership that positively influences and changes not only the leader, but also those with whom they work and interact, as well as their organization as a whole.</p>

  <h2 class="abs sec-title" style="left:64px;top:591px;width:748px">Our services</h2>

  <div class="abs" style="left:64px;top:617px;width:225px">
    <div class="service-photo" role="img" aria-label="Photo of a presenter at a whiteboard in a boardroom meeting" style="background:linear-gradient(135deg,#d9dde6,#7b7c8e 45%,#4a3c52 75%,#c7cbd6)"></div>
    <h3 class="service-title lead" style="margin-top:9px">Leadership Coaching</h3>
    <p class="service-sub">"Everyone has a plan until they get punched in the face."</p>
    <p class="service-text">The Stream of Consciousness, flows through only a few of the world's best organizations and is fed by creative and positive thinking that produces questions like:</p>
    <p class="read-more lead" style="margin-top:5px">Read more »</p>
  </div>

  <div class="abs" style="left:326px;top:617px;width:225px">
    <div class="service-photo" role="img" aria-label="Black and white photo of colleagues reviewing work at a laptop" style="background:linear-gradient(120deg,#e6e6e6,#8d8d8d 40%,#3a3a3a 65%,#cfcfcf)"></div>
    <h3 class="service-title" style="margin-top:9px">Assessments</h3>
    <p class="service-sub">You Are Here!</p>
    <p class="service-text">Great coaching relationships start by meeting the client where they are. We use an array of assessment tools, both attitudinal and personality,</p>
    <p class="read-more" style="margin-top:5px">Read more »</p>
  </div>

  <div class="abs" style="left:587px;top:617px;width:225px">
    <div class="service-photo" role="img" aria-label="Black and white photo of business people shaking hands across a desk" style="background:linear-gradient(120deg,#5a5a5a,#bdbdbd 35%,#444 60%,#e2e2e2)"></div>
    <h3 class="service-title" style="margin-top:9px">Skills Coaching</h3>
    <p class="service-sub">Building Capabilities and Capacity</p>
    <p class="service-text">Most organizations invest in "training" their employees with the intention of increasing their productivity, their value to the organization,</p>
    <p class="read-more" style="margin-top:5px">Read more »</p>
  </div>

  <h2 class="abs sec-title" style="left:64px;top:857px;width:350px">Ask yourself:</h2>
  <div class="abs ask-item" style="top:883px"><span class="ask-mark"></span><span>Has my company lost it's momentum? Is it stuck in neutral or worse?</span></div>
  <div class="abs ask-item" style="top:909px"><span class="ask-mark"></span><span>Am I frustrated by the lack of cooperation and general apathy among my people?</span></div>
  <div class="abs ask-item" style="top:935px"><span class="ask-mark"></span><span>Have I lost my edge as a leader? Am I having trouble getting results applying the skills and energy that worked so well in the past?</span></div>

  <h2 class="abs sec-title" style="left:464px;top:857px;width:290px">Testimonials</h2>
  <div class="abs slide-btn on" style="left:760px;top:858px"><svg width="9" height="10" viewBox="0 0 9 10"><path d="M7 1 L2 5 L7 9" fill="none" stroke="#fff" stroke-width="2.2"/></svg></div>
  <div class="abs slide-btn" style="left:788px;top:858px"><svg width="9" height="10" viewBox="0 0 9 10"><path d="M2 1 L7 5 L2 9" fill="none" stroke="#0355a3" stroke-width="2.2"/></svg></div>
  <p class="abs body-text" style="left:464px;top:883px;width:348px;line-height:13.4px">" Lorem ipsum dolor sit amet, consectetur adipiscing elit. Cras feugiat sectetur ipsum id euismod. Praesent commodo varius nunc, v ulputate&nbsp; Lorem ipsum dolor sit amet, consectetur adipiscing elit. Cras "</p>
  <svg class="abs" style="left:466px;top:932px" width="31" height="33" viewBox="0 0 31 33" aria-label="Client avatar">
    <circle cx="15.5" cy="9" r="7.5" fill="#3f7fc0"/>
    <path d="M1 33 Q1 20 15.5 19 Q30 20 30 33Z" fill="#3f7fc0"/>
  </svg>
  <p class="abs" style="right:66px;top:941px;font-size:8.2px;color:var(--dark)">Lorem lipsum , <span style="color:var(--blue)">dolor sit</span></p>

  <div class="abs footer"></div>

  <h3 class="abs foot-title" style="left:64px;top:1020px;width:173px">Our address</h3>
  <div class="abs foot-row" style="left:64px;top:1041px">
    <svg width="13" height="12" viewBox="0 0 13 12"><path d="M6.5 1 L12 6 H10 V11 H7.5 V8 H5.5 V11 H3 V6 H1Z" fill="#6b7a88"/></svg>
    <span>218 Quayside Avenue Suite 40-B<br>Marlow, VA 20999</span>
  </div>
  <div class="abs foot-row" style="left:64px;top:1077px">
    <svg width="12" height="12" viewBox="0 0 14 14"><path d="M3 1 L5.5 4 L4 6 Q5.5 9 8 10 L10 8.5 L13 11 L11 13.5 Q5 13 1 4 Z" fill="#6b7a88"/></svg>
    <span>(555) 014-7720</span>
  </div>
  <div class="abs foot-row" style="left:64px;top:1101px">
    <svg width="13" height="11" viewBox="0 0 13 11"><rect x="3" y="1" width="7" height="4" fill="none" stroke="#6b7a88" stroke-width="1.3"/><rect x="1" y="5" width="11" height="5" fill="#6b7a88"/></svg>
    <span>(555) 014-3381</span>
  </div>
  <div class="abs foot-row" style="left:64px;top:1125px">
    <svg width="13" height="10" viewBox="0 0 13 10"><rect x="1" y="1" width="11" height="8" fill="#6b7a88"/><path d="M1 1 L6.5 5.5 L12 1" fill="none" stroke="#eef3f8" stroke-width="1.1"/></svg>
    <span>info@harborlanecoach.example</span>
  </div>

  <h3 class="abs foot-title" style="left:316px;top:1020px;width:210px">Social Feed widget</h3>
  <div class="abs foot-row" style="left:318px;top:1041px;width:216px">
    <span style="width:12px;height:12px;border-radius:50%;background:#6b7a88;flex:none"></span>
    <span>Lorem ipsum dolor sit amet, consectetur ing elit. Cras vel odio <b style="color:var(--dark);font-style:italic;font-weight:600">vitae tellus</b> convallis bibendum nec sed mi.<br><i style="color:var(--blue);font-weight:600">about 6 day ago</i></span>
  </div>
  <h3 class="abs foot-title" style="left:316px;top:1099px;width:210px">Get in touch</h3>
  <div class="abs" style="left:320px;top:1117px;display:flex;gap:8px" aria-label="Social links">
    <span class="social first"></span><span class="social"></span><span class="social"></span><span class="social"></span>
  </div>

  <h3 class="abs foot-title" style="left:608px;top:1020px;width:204px">Conatct us</h3>
  <div class="abs field" style="left:608px;top:1039px;width:102px">Fist name</div>
  <div class="abs field" style="left:712px;top:1039px;width:100px">Last name</div>
  <div class="abs field" style="left:608px;top:1059px;width:102px">Email</div>
  <div class="abs field" style="left:712px;top:1059px;width:100px">Phone</div>
  <div class="abs field" style="left:608px;top:1079px;width:204px;height:36px">Message</div>
  <div class="abs submit">Submit</div>

  <div class="abs bottom-bar"></div>
  <p class="abs bottom-links"><span class="cur">Home</span><span class="sep">/</span>About Us<span class="sep">/</span>Why coaching<span class="sep">/</span>Services<span class="sep">/</span>Clients<span class="sep">/</span>Resources<span class="sep">/</span>Blog<span class="sep">/</span>Contact Us</p>
  <p class="abs copyright">Copyright © 2014 Harbor Lane Coaching.</p>
  <div class="abs copy-dot"></div>

</div>
</body>
</html>
```